New Automotive supply business in need of label designs for additive range

I need front and back label design for about 12 different variety of products. They are all to do with the Automotive additive industry such as Petrol injector cleaner, Engine Flush, Oil treatments etc. I will provide overall measurements of the label in the brief as well as examples of artwork that I like. Label must comply with local regulations, i can assist you with this. We will start with one product only, and if successful I am happy to hire you to do the remainder of the project. I would like to see designs that use my company logo colors. These products are for the workshop industry only (not retail) so does not have to be too animated.You will see my logo designs under the name "kalmor" in the uploaded files.Product Name is : Motor Prime & Renew
Front Label must say:PREPARES ENGINES FOR NEW OIL
RESTORES COMPRESSION
MINIMISES CONTAMINATION WITH NEW OIL
CONTAINS KALMOR TUFFLINE PROTECTION
RECOMMENDED FOR PETROL, DIESEL AND HYBRID ENGINES
350ML
Dimensions of metal can that will be used for label is : 175mm in height and 56mm in diameter. IN THE UPLOADED FILES YOU WILL SEE A SAMPLE OF THE ACTUAL CAN TO BE USED.
I have now included an example of a shield/guard that should be shown on the rear of the label if possible, im happy if you come up with your own shield designs.

Target Market(s)

Mechanics

Industry/Entity Type

Automotive Part

Requirements
Must have
• My logo on top
Nice to have
• Silver background
Should not have
• Pictures of engines or engine parts etc

```html
<!DOCTYPE html>
<html lang="en">
<head>
<meta charset="utf-8">
<title>Kalmor – Motor Prime &amp; Renew front label</title>
<link rel="stylesheet" href="https://fonts.googleapis.com/css2?family=Roboto+Condensed:ital,wght@0,400;0,700;1,800&family=Roboto:wght@400&display=swap">
<style>
  :root{
    --page:#f3f3f3;
    --black:#1f1f1f;
    --black-soft:#2c2c2c;
    --silver-light:#ffffff;
    --silver-mid:#d9d9d9;
    --silver-dark:#a9a9a9;
    --blue:#2a8ad3;
    --blue-deep:#1f78c2;
    --ink:#2a2a2a;
    --bullet-ink:#1c2a38;
    --brand-blue:#3f9ae6;
    --accent-orange:#f28c38;
  }
  *{box-sizing:border-box;margin:0;padding:0}
  html,body{width:1200px;height:1200px;overflow:hidden;background:var(--page)}
  body{display:flex;align-items:center;justify-content:center}

  .label{
    position:relative;
    width:440px;height:1000px;
    background:linear-gradient(90deg,var(--silver-dark) 0%,var(--silver-mid) 8%,var(--silver-light) 30%,var(--silver-light) 70%,var(--silver-mid) 92%,var(--silver-dark) 100%);
    overflow:hidden;
    font-family:"Roboto Condensed",sans-serif;
  }

  .label__header{
    position:absolute;left:0;top:0;width:100%;height:290px;
    background:var(--black);
    border-bottom-left-radius:50% 46px;
    border-bottom-right-radius:50% 46px;
    box-shadow:0 6px 0 var(--silver-dark);
    display:flex;flex-direction:column;align-items:center;justify-content:center;gap:14px;
  }
  .brand{display:flex;align-items:center;gap:14px}
  .brand__dot{width:30px;height:30px;border-radius:50%;background:var(--accent-orange)}
  .brand__name{
    font-weight:700;font-size:64px;letter-spacing:3px;color:var(--brand-blue);line-height:1;
  }
  .brand__tagline{
    font-size:15px;letter-spacing:1.5px;color:#e6e6e6;
    border-top:2px solid var(--accent-orange);padding-top:6px;
  }

  .label__title{
    position:absolute;left:0;top:330px;width:100%;
    text-align:center;
    font-weight:800;font-style:italic;
    font-size:70px;line-height:1.08;color:var(--ink);
  }

  .label__claims{
    position:absolute;left:0;top:528px;width:100%;height:290px;
    background:linear-gradient(180deg,var(--blue) 0%,var(--blue-deep) 100%);
    border-top:8px solid var(--silver-mid);
    border-bottom:8px solid var(--silver-mid);
    list-style:none;
    padding:22px 10px 0 6px;
    display:flex;flex-direction:column;gap:14px;
  }
  .label__claims li{
    font-size:20px;color:var(--bullet-ink);text-transform:uppercase;line-height:1.1;
  }
  .label__claims li::before{content:"-"}
  .label__claims strong{font-weight:700}

  .label__volume{
    position:absolute;left:12px;right:12px;top:826px;height:100px;
    background:var(--black-soft);
    border-bottom-left-radius:60px 90px;
    border-bottom-right-radius:60px 90px;
    display:flex;align-items:center;justify-content:center;
    font-family:"Roboto",sans-serif;font-size:52px;color:#e9e9e9;
  }
</style>
</head>
<body>
  <section class="label" aria-label="Kalmor Motor Prime and Renew front label">
    <header class="label__header">
      <div class="brand">
        <span class="brand__dot"></span>
        <span class="brand__name">KALMOR</span>
      </div>
      <div class="brand__tagline">DRIVE WITH KALMOR</div>
    </header>

    <h1 class="label__title">MOTOR PRIME<br>&amp; RENEW</h1>

    <ul class="label__claims">
      <li>Prepares engines <strong>for new oil</strong></li>
      <li>Restores compression</li>
      <li>Minimises contamination <strong>with new oil</strong></li>
      <li>Contains kalmor <strong>tuffline protection</strong></li>
      <li>Recommended <strong>for petrol, diesel,</strong> and</li>
      <li>Hybrid engines</li>
    </ul>

    <div class="label__volume">350 ml</div>
  </section>
</body>
</html>
```